Yacht, Boats, Watersports company needs a redesign of business card

Hello Designers!
We are a Boat dealership company that sells fun in the water, we sell boats, Yachts, Kayaks and also yacht WaterSport toys. We are looking to redesign our business cards in to something a little bit more sophisticated. in a way that we can make better use of our company colors. I'm attaching a zipped file containing the company 3 sets of company logo which one is an horizontal another one is a vertical and also a chromed 3d logo. Also is included two set of business cards that we use and also some designs that i think it's interesting. We use PMS 2026c Orange and PMS 7687C Blue. I would like to see at least two different options with the orange as accent and also using blue as an accent color. It's really important for the business cards to have a font option and size that is legible to most people. Our current website is wwww.corvellamarine.com. Please visit if you want to have a better feeling of the Boat dealership
You can send Single sided or double side options. We are now using single sided but we may be open for a double side option if we really like the design.
Target Market(s)
Marine, boat sales, yacht sales, water toys sales/
Contact Information for Business Card
Name: Dale Pritchett
Address: 718 West Halden Lane,
Dania Beach, FL 33019
Phone: 954-382-7146
Fax: 954:382-7139
Cell: 954-451-8320
Email: 212@corvellamarine.com
Website: corvellamarine.com
Requirements
Must have
- the current information of the business card provided.
logo
use the PMS Colors
Nice to have
- a touch of elegance and sophistication but simple
Should not have
- should not have any typography that is hard to read, the card should be simple but yet sophisticated.

```html
<!DOCTYPE html>
<html lang="en">
<head>
<meta charset="utf-8">
<title>Corvella Marine — Business Card</title>
<link href="https://fonts.googleapis.com/css2?family=Arimo:wght@700&family=PT+Sans+Narrow:wght@400&display=swap" rel="stylesheet">
<style>
  :root {
    --brand-orange: #f37021;
    --brand-blue: #1552a9;
    --brand-navy: #1b3a7a;
    --card-white: #ffffff;
    --backdrop: #efefed;
    --text-light: #ffffff;
  }
  * { margin: 0; padding: 0; box-sizing: border-box; }
  html, body { width: 1200px; height: 1200px; overflow: hidden; }
  body {
    background: var(--backdrop);
    position: relative;
    font-family: "PT Sans Narrow", "Arial Narrow", sans-serif;
  }
  .card {
    position: absolute;
    top: 232px;
    width: 420px;
    height: 735px;
    overflow: hidden;
    box-shadow: 0 18px 40px rgba(0,0,0,0.14);
  }
  .card-front { left: 150px; background: var(--card-white); }
  .card-back { left: 630px; background: var(--brand-blue); }
  .card-shape { position: absolute; inset: 0; width: 420px; height: 735px; }

  .brand {
    position: absolute;
    top: 190px;
    left: 0;
    width: 100%;
    text-align: center;
  }
  .brand-mark {
    display: block;
    width: 58px;
    height: 58px;
    margin: 0 auto 22px;
    border: 6px solid var(--brand-orange);
    border-radius: 50%;
  }
  .brand-name {
    font-family: "Arimo", Arial, sans-serif;
    font-weight: 700;
    font-size: 30px;
    letter-spacing: 1px;
    color: var(--brand-navy);
  }
  .website {
    position: absolute;
    top: 648px;
    left: 0;
    width: 100%;
    display: flex;
    justify-content: center;
    align-items: center;
    gap: 8px;
    color: var(--text-light);
    font-size: 27px;
  }

  .holder-name {
    position: absolute;
    top: 182px;
    left: 0;
    width: 100%;
    text-align: center;
    font-family: "Arimo", Arial, sans-serif;
    font-weight: 700;
    font-size: 32px;
    color: var(--text-light);
  }
  .contact-row {
    position: absolute;
    left: 92px;
    display: flex;
    align-items: center;
    gap: 18px;
    color: var(--text-light);
    font-size: 19px;
    line-height: 1.2;
  }
  .contact-row svg { flex: none; }
  .contact-label { width: 32px; }
  .row-address { top: 318px; }
  .row-phone { top: 412px; }
  .row-fax { top: 490px; }
  .row-cell { top: 570px; }
  .row-email { top: 652px; }
</style>
</head>
<body>

  <section class="card card-front">
    <svg class="card-shape" viewBox="0 0 420 735" aria-hidden="true">
      <polygon points="0,433 223,331 420,404 420,735 0,735" fill="var(--brand-orange)"/>
    </svg>
    <div class="brand">
      <span class="brand-mark"></span>
      <div class="brand-name">CORVELLA MARINE</div>
    </div>
    <div class="website">
      <svg width="22" height="22" viewBox="0 0 22 22" aria-hidden="true">
        <circle cx="11" cy="11" r="9" fill="none" stroke="#fff" stroke-width="2"/>
        <ellipse cx="11" cy="11" rx="4" ry="9" fill="none" stroke="#fff" stroke-width="1.5"/>
        <line x1="2" y1="11" x2="20" y2="11" stroke="#fff" stroke-width="1.5"/>
      </svg>
      <span>corvellamarine.com</span>
    </div>
  </section>

  <section class="card card-back">
    <svg class="card-shape" viewBox="0 0 420 735" aria-hidden="true">
      <polygon points="0,0 420,0 420,42 223,132 0,44" fill="var(--brand-orange)"/>
    </svg>
    <h1 class="holder-name">Dale Pritchett</h1>

    <div class="contact-row row-address">
      <svg width="26" height="32" viewBox="0 0 26 32" aria-hidden="true">
        <path d="M13 2a10 10 0 0 1 10 10c0 8-10 18-10 18S3 20 3 12A10 10 0 0 1 13 2z" fill="none" stroke="#fff" stroke-width="2"/>
        <circle cx="13" cy="12" r="3.5" fill="none" stroke="#fff" stroke-width="2"/>
      </svg>
      <span>Address: 718 West Halden Lane,<br>Dania Beach, FL 33019</span>
    </div>

    <div class="contact-row row-phone">
      <svg width="28" height="28" viewBox="0 0 28 28" aria-hidden="true">
        <circle cx="14" cy="14" r="11" fill="none" stroke="#fff" stroke-width="2"/>
        <path d="M10 9c0 5 4 9 9 9l1-2-3-2-1 1c-2-1-3-2-4-4l1-1-2-3z" fill="#fff"/>
      </svg>
      <span>954-382-7146</span>
    </div>

    <div class="contact-row row-fax">
      <span class="contact-label">Fax</span>
      <span>954:382-7139</span>
    </div>

    <div class="contact-row row-cell">
      <svg width="28" height="34" viewBox="0 0 28 34" aria-hidden="true">
        <rect x="7" y="2" width="14" height="28" rx="2" fill="none" stroke="#fff" stroke-width="1.8"/>
        <line x1="12" y1="26" x2="16" y2="26" stroke="#fff" stroke-width="1.8"/>
      </svg>
      <span>954-451-8320</span>
    </div>

    <div class="contact-row row-email">
      <svg width="28" height="28" viewBox="0 0 28 28" aria-hidden="true">
        <circle cx="14" cy="14" r="11" fill="none" stroke="#fff" stroke-width="2"/>
        <circle cx="14" cy="14" r="5" fill="none" stroke="#fff" stroke-width="2"/>
        <path d="M19 11v5c0 2 3 2 3 0" fill="none" stroke="#fff" stroke-width="2"/>
      </svg>
      <span>212@corvellamarine.com</span>
    </div>
  </section>

</body>
</html>
```